Webpage

I am a professional genealogist. I need a webpage that is professional looking (using the logo I chose), I can add hyperlinks and photos to if and when I want.

```html
<!DOCTYPE html>
<html lang="en">
<head>
<meta charset="utf-8">
<title>Mara Whitlock — Professional Genealogist</title>
<link href="https://fonts.googleapis.com/css2?family=Open+Sans:wght@400;600;700;800&family=Open+Sans+Condensed:wght@700&display=swap" rel="stylesheet">
<style>
:root{
  --green:#7cc4a0;
  --green-dark:#5eaa86;
  --ink:#333;
  --muted:#888;
  --light:#f1f1f1;
  --dark:#2f2f2f;
  --darker:#232323;
  --orange:#f7941d;
  --yellow:#f2c100;
  --blue:#3a9ad9;
  --skill-green:#82c59f;
}
*{box-sizing:border-box;margin:0;padding:0}
html,body{width:1200px;height:4000px;overflow:hidden}
body{font-family:"Open Sans",Arial,sans-serif;color:var(--ink);background:#fff;position:relative}
section,header,footer,.topbar{position:absolute;left:0;width:1200px}
.section-title{position:absolute;left:0;width:1200px;text-align:center;font-size:30px;font-weight:700;color:#333;letter-spacing:1px;font-family:"Open Sans Condensed","Open Sans",sans-serif}
.section-title::after{content:"";display:block;width:180px;height:2px;background:#ddd;margin:16px auto 0}

/* top bar */
.topbar{top:0;height:56px;background:var(--green);color:#fff;font-size:13px}
.topbar .contact{position:absolute;left:127px;top:0;height:56px;display:flex;align-items:center;gap:40px}
.topbar .contact span{display:flex;align-items:center;gap:10px}
.topbar .search{position:absolute;right:0;top:0;width:233px;height:56px;background:#3b3b3b;display:flex;align-items:center;justify-content:flex-end;padding-right:120px}

/* header */
.site-header{top:56px;height:127px;background:#fff}
.brand{position:absolute;left:127px;top:33px;display:flex;align-items:center;gap:14px}
.brand-mark{width:60px;height:60px;border-radius:50%;background:var(--green)}
.brand-name{font-size:20px;font-weight:400;color:#555;line-height:1.1;width:190px}
.main-nav{position:absolute;right:127px;top:0;height:127px;display:flex;align-items:center;gap:26px;font-size:14px;font-weight:600;color:#444}
.main-nav a{color:inherit;text-decoration:none;padding-bottom:4px;border-bottom:2px solid transparent}
.main-nav a.active{color:var(--green);border-bottom-color:var(--green)}

/* hero */
.hero{top:183px;height:450px}
.hero-photo{position:absolute;inset:0;background:linear-gradient(100deg,#b9d8e6 0%,#dbe9ef 45%,#9fb9c8 75%,#e8eef0 100%)}
.hero-card{position:absolute;left:127px;top:100px;width:473px;height:250px;background:rgba(124,196,160,.92);color:#fff;padding:26px 30px}
.hero-card h1{font-size:46px;font-weight:700;line-height:1;letter-spacing:1px}
.hero-card h2{font-size:24px;font-weight:700;margin-top:8px;letter-spacing:1px}
.hero-card p{font-size:14px;line-height:1.4;margin-top:12px;width:380px}
.hero-card .more{display:inline-flex;align-items:center;gap:10px;margin-top:14px;font-size:13px;background:rgba(0,0,0,.12);padding:6px 12px}

/* services */
.services{top:633px;height:394px;border-bottom:1px solid #e6e6e6}
.services .section-title{top:40px}
.arrow{position:absolute;width:22px;height:22px;border-radius:50%;background:#ccc}
.service{position:absolute;top:140px;width:280px;text-align:center}
.service-icon{width:100px;height:100px;border-radius:50%;background:var(--green);margin:0 auto;display:flex;align-items:center;justify-content:center}
.service h3{font-size:16px;font-weight:700;margin-top:24px;color:#333}
.service p{font-size:12px;color:var(--muted);margin-top:12px;line-height:1.5}

/* work */
.work{top:1027px;height:640px;background:var(--light)}
.work .section-title{top:45px}
.work-grid{position:absolute;left:127px;top:140px;width:946px;height:426px;display:grid;grid-template-columns:repeat(3,1fr);grid-template-rows:repeat(2,1fr);gap:4px}
.work-tile{background:linear-gradient(135deg,#cfe1e9,#8fb2c4)}
.work-tile:nth-child(2){background:linear-gradient(135deg,#9cbfcf,#e0ebef)}
.work-tile:nth-child(3){background:linear-gradient(135deg,#dfe9ee,#a7c1cd)}
.work-tile:nth-child(5){background:linear-gradient(135deg,#a8c7d4,#e5eef1)}
.work-tile:nth-child(6){background:linear-gradient(135deg,#e0e9ed,#9db6c3)}
.work-feature{background:var(--green);color:#fff;padding:130px 34px 0}
.work-feature h3{font-size:18px;font-weight:700;letter-spacing:1px}
.work-feature span{display:inline-block;margin-top:40px;font-size:12px;background:rgba(0,0,0,.12);padding:5px 12px}

/* cta band */
.cta{top:1667px;height:150px;background:linear-gradient(90deg,#3a3a3a,#555 50%,#3c3c3c)}
.cta p{position:absolute;left:127px;top:55px;color:#fff;font-size:29px;font-weight:700;font-family:"Open Sans Condensed","Open Sans",sans-serif;letter-spacing:.5px}
.cta .button{position:absolute;right:127px;top:52px;background:var(--green);color:#fff;font-size:17px;font-weight:700;padding:10px 20px}

/* skills */
.skills{top:1817px;height:500px;background:var(--light)}
.skills .section-title{top:60px}
.skills .lede{position:absolute;top:120px;width:1200px;text-align:center;font-size:12px;color:var(--muted)}
.skill{position:absolute;top:150px;width:220px;text-align:center}
.skill h3{font-size:22px;font-weight:700;margin-top:24px;color:#333}

/* team */
.team{top:2317px;height:643px;background:#fff}
.team .section-title{top:68px}
.member{position:absolute;top:133px;width:257px}
.member-photo{height:327px;background:linear-gradient(180deg,#eef2f4,#bfd0da)}
.member h3{font-size:15px;font-weight:700;margin-top:36px}
.member p{font-size:14px;color:#555;margin-top:10px}
.member .social{position:absolute;right:0;top:373px;display:flex;gap:8px}
.dot{width:20px;height:20px;border-radius:50%;background:var(--green)}

/* stats */
.stats{top:2960px;height:490px;background:linear-gradient(160deg,#262626,#4a4a4a 50%,#2b2b2b)}
.stats .section-title{top:45px;color:#fff}
.stats .section-title::after{background:rgba(255,255,255,.3)}
.stats .lede{position:absolute;top:110px;width:1200px;text-align:center;font-size:12px;color:#ccc}
.stat{position:absolute;top:170px;width:260px;text-align:center;color:#fff}
.stat .num{font-size:64px;font-weight:700;margin-top:20px;line-height:1.1}
.stat h3{font-size:20px;font-weight:700;margin-top:14px;letter-spacing:1px}

/* partners */
.partners{top:3450px;height:200px;background:#fff}
.partner{position:absolute;top:82px;width:170px;text-align:center;font-size:22px;font-weight:700;color:#555}

/* footer */
.site-footer{top:3650px;height:300px;background:#3a3a3a;color:#ccc;font-size:12px}
.site-footer h4{color:#fff;font-size:15px;font-weight:700;margin-bottom:20px}
.footer-col{position:absolute;top:40px;line-height:1.6}
.tweet{background:#4a4a4a;padding:8px 10px;margin-bottom:8px;width:220px}
.subscribe{display:flex;margin-top:18px}
.subscribe span{display:block;height:36px;line-height:36px;padding:0 12px}
.subscribe .field{background:#fff;color:#999;width:170px}
.subscribe .send{background:var(--green);color:#fff}
.bottom-bar{position:absolute;left:0;top:3950px;width:1200px;height:50px;background:var(--darker);color:#999;font-size:12px}
.bottom-bar .copy{position:absolute;left:127px;top:17px}
.bottom-bar .links{position:absolute;left:420px;top:17px;display:flex;gap:30px}
.bottom-bar .social{position:absolute;right:127px;top:14px;display:flex;gap:8px}
.bottom-bar .social .dot{background:#777}
</style>
</head>
<body>

<div class="topbar">
  <div class="contact">
    <span><svg width="14" height="14" viewBox="0 0 24 24"><path fill="#fff" d="M6.6 10.8a15 15 0 0 0 6.6 6.6l2.2-2.2a1 1 0 0 1 1-.25 11.4 11.4 0 0 0 3.6.6 1 1 0 0 1 1 1V20a1 1 0 0 1-1 1A17 17 0 0 1 3 4a1 1 0 0 1 1-1h3.5a1 1 0 0 1 1 1c0 1.25.2 2.45.6 3.6a1 1 0 0 1-.25 1z"/></svg>555-208-4417</span>
    <span><svg width="14" height="12" viewBox="0 0 24 20"><rect x="1" y="1" width="22" height="18" fill="none" stroke="#fff" stroke-width="2"/><path d="M1 1l11 9 11-9" fill="none" stroke="#fff" stroke-width="2"/></svg>mara@whitlockresearch.example</span>
  </div>
  <div class="search"><svg width="16" height="16" viewBox="0 0 24 24"><circle cx="10" cy="10" r="7" fill="none" stroke="#fff" stroke-width="2.5"/><path d="M15 15l6 6" stroke="#fff" stroke-width="2.5"/></svg></div>
</div>

<header class="site-header">
  <div class="brand"><div class="brand-mark"></div><div class="brand-name">Whitlock Research Services</div></div>
  <nav class="main-nav">
    <a class="active" href="#">HOME</a><a href="#">ABOUT</a><a href="#">SERVICES</a><a href="#">CONTACT</a><a href="#">PUBLICATIONS</a><a href="#">BLOG</a><a href="#">LINKS</a>
  </nav>
</header>

<section class="hero">
  <div class="hero-photo" role="img" aria-label="Photo of a scientist examining a sample in a laboratory"></div>
  <div class="hero-card">
    <h1>MARA WHITLOCK</h1>
    <h2>PROFESSIONAL GENEALOGIST</h2>
    <p>Lorem ipsum dolor sit amet voluptatem fugit aut illo omnis explicabo ipsa ipsa, nemo enim quam dolorem beatae magni architecto nisi.</p>
    <div class="more">learn more <svg width="14" height="14" viewBox="0 0 24 24"><circle cx="12" cy="12" r="11" fill="#fff"/><path d="M10 7l5 5-5 5" fill="none" stroke="#7cc4a0" stroke-width="2.5"/></svg></div>
  </div>
</section>

<section class="services">
  <h2 class="section-title">OUR SERVICES</h2>
  <div class="arrow" style="left:127px;top:180px"></div>
  <div class="arrow" style="right:127px;top:180px"></div>
  <div class="service" style="left:180px">
    <div class="service-icon"><svg width="48" height="48" viewBox="0 0 48 48"><circle cx="24" cy="24" r="20" fill="none" stroke="#fff" stroke-width="4"/><circle cx="24" cy="24" r="7" fill="#fff"/></svg></div>
    <h3>FORENSIC GENEALOGY</h3>
    <p>Voluptatem doloremque porqui beatae ratione dolores dolores unde</p>
  </div>
  <div class="service" style="left:460px">
    <div class="service-icon"><svg width="48" height="48" viewBox="0 0 48 48"><rect x="8" y="8" width="32" height="32" rx="4" fill="none" stroke="#fff" stroke-width="4"/><rect x="18" y="18" width="12" height="12" fill="#fff"/></svg></div>
    <h3>KINSHIP DETERMINATION</h3>
    <p>Voluptatem doloremque porqui beatae ratione dolores dolores unde</p>
  </div>
  <div class="service" style="left:740px">
    <div class="service-icon"><svg width="48" height="48" viewBox="0 0 48 48"><circle cx="21" cy="21" r="12" fill="none" stroke="#fff" stroke-width="4"/><path d="M30 30l10 10" stroke="#fff" stroke-width="5"/></svg></div>
    <h3>RESEARCH ANALYSIS</h3>
    <p>Voluptatem doloremque porqui beatae ratione dolores dolores unde</p>
  </div>
</section>

<section class="work">
  <h2 class="section-title">OUR WORK</h2>
  <div class="work-grid">
    <div class="work-tile" role="img" aria-label="Photo of a researcher with a test tube"></div>
    <div class="work-tile" role="img" aria-label="Photo of a team working in a laboratory"></div>
    <div class="work-tile" role="img" aria-label="Photo of a researcher at a microscope"></div>
    <div class="work-feature"><h3>DOLORES VOLUPTATEM</h3><span>View More</span></div>
    <div class="work-tile" role="img" aria-label="Photo of researchers reviewing samples"></div>
    <div class="work-tile" role="img" aria-label="Photo of two scientists at microscopes"></div>
  </div>
</section>

<section class="cta" role="img" aria-label="Dark city skyline backdrop">
  <p>LOREM IPSUM DOLOR SIT AMET REM EOS ILLO OMNIS AUT</p>
  <div class="button">MAKE AN APPOINTMENT</div>
</section>

<section class="skills">
  <h2 class="section-title">OUR SKILLS</h2>
  <p class="lede">Beatae quaeratione ratione dolores beatae quia ratione dolores unde quas dolorem unde quae dolore</p>

  <div class="skill" style="left:110px">
    <svg width="220" height="220" viewBox="0 0 220 220"><circle cx="110" cy="110" r="95" fill="none" stroke="#fff" stroke-width="20"/><circle cx="110" cy="110" r="95" fill="none" stroke="var(--orange)" stroke-width="20" stroke-dasharray="448 597" transform="rotate(-90 110 110)"/><circle cx="110" cy="110" r="72" fill="none" stroke="var(--orange)" stroke-width="14"/><circle cx="110" cy="110" r="62" fill="#fff"/><text x="110" y="122" text-anchor="middle" font-family="Open Sans, sans-serif" font-size="36" font-weight="700" fill="#444">75%</text></svg>
    <h3>RESEARCH</h3>
  </div>
  <div class="skill" style="left:367px">
    <svg width="220" height="220" viewBox="0 0 220 220"><circle cx="110" cy="110" r="95" fill="none" stroke="#fff" stroke-width="20"/><circle cx="110" cy="110" r="95" fill="none" stroke="var(--skill-green)" stroke-width="20" stroke-dasharray="507 597" transform="rotate(-90 110 110)"/><circle cx="110" cy="110" r="72" fill="none" stroke="var(--skill-green)" stroke-width="14"/><circle cx="110" cy="110" r="62" fill="#fff"/><text x="110" y="122" text-anchor="middle" font-family="Open Sans, sans-serif" font-size="36" font-weight="700" fill="#444">85%</text></svg>
    <h3>ANALYSIS</h3>
  </div>
  <div class="skill" style="left:613px">
    <svg width="220" height="220" viewBox="0 0 220 220"><circle cx="110" cy="110" r="95" fill="none" stroke="#fff" stroke-width="20"/><circle cx="110" cy="110" r="95" fill="none" stroke="var(--yellow)" stroke-width="20" stroke-dasharray="358 597" transform="rotate(-90 110 110)"/><circle cx="110" cy="110" r="72" fill="none" stroke="var(--yellow)" stroke-width="14"/><circle cx="110" cy="110" r="62" fill="#fff"/><text x="110" y="122" text-anchor="middle" font-family="Open Sans, sans-serif" font-size="36" font-weight="700" fill="#444">60%</text></svg>
    <h3>CONSULTATION</h3>
  </div>
  <div class="skill" style="left:863px">
    <svg width="220" height="220" viewBox="0 0 220 220"><circle cx="110" cy="110" r="95" fill="none" stroke="#fff" stroke-width="20"/><circle cx="110" cy="110" r="95" fill="none" stroke="var(--blue)" stroke-width="20" stroke-dasharray="537 597" transform="rotate(-90 110 110)"/><circle cx="110" cy="110" r="72" fill="none" stroke="var(--blue)" stroke-width="14"/><circle cx="110" cy="110" r="62" fill="#fff"/><text x="110" y="122" text-anchor="middle" font-family="Open Sans, sans-serif" font-size="36" font-weight="700" fill="#444">90%</text></svg>
    <h3>RECORD RETRIEVAL</h3>
  </div>
</section>

<section class="team">
  <h2 class="section-title">MEET OUR TEAM</h2>
  <div class="member" style="left:167px">
    <div class="member-photo" role="img" aria-label="Portrait photo of a team member in a lab coat"></div>
    <h3>JHONE DOE</h3><p>Research</p>
    <div class="social"><span class="dot"></span><span class="dot"></span><span class="dot"></span></div>
  </div>
  <div class="member" style="left:470px">
    <div class="member-photo" role="img" aria-label="Portrait photo of a team member in safety glasses"></div>
    <h3>JAMES DOE</h3><p>Consultant</p>
    <div class="social"><span class="dot"></span><span class="dot"></span><span class="dot"></span></div>
  </div>
  <div class="member" style="left:777px">
    <div class="member-photo" role="img" aria-label="Portrait photo of a team member in a lab coat"></div>
    <h3>ALVIN DOE</h3><p>Analist</p>
    <div class="social"><span class="dot"></span><span class="dot"></span><span class="dot"></span></div>
  </div>
</section>

<section class="stats" role="img" aria-label="Aerial city photo backdrop">
  <h2 class="section-title">OUR STATS</h2>
  <p class="lede">Dolores voluptatem doloremque porqui beatae quaeratione ratione beatae quia ratione dolores unde</p>
  <div class="stat" style="left:160px">
    <svg width="64" height="64" viewBox="0 0 48 48"><circle cx="20" cy="20" r="13" fill="none" stroke="#fff" stroke-width="5"/><path d="M30 30l12 12" stroke="#fff" stroke-width="6" stroke-linecap="round"/></svg>
    <div class="num">987</div><h3>RESEARCH</h3>
  </div>
  <div class="stat" style="left:470px">
    <svg width="64" height="64" viewBox="0 0 48 48"><rect x="8" y="6" width="32" height="38" rx="3" fill="#fff"/><rect x="17" y="2" width="14" height="8" rx="2" fill="#fff"/><path d="M15 26l6 6 12-12" fill="none" stroke="#333" stroke-width="4"/></svg>
    <div class="num">543</div><h3>CONSULTATION</h3>
  </div>
  <div class="stat" style="left:780px">
    <svg width="64" height="64" viewBox="0 0 48 48"><circle cx="24" cy="14" r="10" fill="#fff"/><path d="M6 46c0-12 8-20 18-20s18 8 18 20z" fill="#fff"/></svg>
    <div class="num">135</div><h3>CLIENTS</h3>
  </div>
</section>

<section class="partners">
  <div class="arrow" style="left:127px;top:90px"></div>
  <div class="arrow" style="right:127px;top:90px"></div>
  <div class="partner" style="left:175px">Harborline</div>
  <div class="partner" style="left:350px">Norvik</div>
  <div class="partner" style="left:515px">Caldera</div>
  <div class="partner" style="left:680px">Cityvale</div>
  <div class="partner" style="left:850px">Toonfield</div>
</section>

<footer class="site-footer">
  <div class="footer-col" style="left:127px;width:180px">
    <h4>ABOUT US</h4>
    <p>Fugit aut illo omnis explicabo ipsa, nemo ipsam quasi dolores voluptatem dolor perspiciatis beatae magni architecto nisi.</p>
    <p style="margin-top:20px">Read More</p>
  </div>
  <div class="footer-col" style="left:360px;width:200px">
    <h4>ADDRESS</h4>
    <p>Mara Whitlock<br>Professional Genealogist<br>PO Box 4821<br>Cedar Falls, TX 70000-4821<br>555-208-4417</p>
    <p style="margin-top:20px">Open in Maps</p>
  </div>
  <div class="footer-col" style="left:563px;width:260px">
    <h4>RECENT TWEET</h4>
    <div class="tweet">@dolore maxime dolor sit amet</div>
    <div class="tweet">@dolore maxime dolor sit amet</div>
    <p style="margin-top:12px">View More</p>
  </div>
  <div class="footer-col" style="left:823px;width:250px">
    <h4>CONTACT</h4>
    <p>Nemo ipsam quasi dolores voluptatem dolor perspiciatis beatae magni architecto nisi.</p>
    <div class="subscribe"><span class="field">enter your email</span><span class="send">send</span></div>
  </div>
</footer>
<div class="bottom-bar">
  <span class="copy">© 2014 Mara Whitlock. All Rights Reserved.</span>
  <div class="links"><span>about us</span><span>term and use</span><span>privacy policy</span><span>FAQs</span><span>contact us</span></div>
  <div class="social"><span class="dot"></span><span class="dot"></span><span class="dot"></span><span class="dot"></span><span class="dot"></span><span class="dot"></span></div>
</div>

</body>
</html>
```